KLT Roofing Pty Ltd

We are a high end residential Roofing company
We would like something silimar to the attached logo with the same color scheme

Target Market(s)

High end residential Builders & Architects

Industry/Entity Type

Residential

```html
<!DOCTYPE html>
<html lang="en">
<head>
<meta charset="utf-8">
<title>KLT Roofing – Business Card</title>
<link rel="stylesheet" href="https://fonts.googleapis.com/css2?family=Lato:wght@400;700&display=swap">
<style>
  :root {
    --backdrop: #e4e4e4;
    --card: #fbfbfb;
    --slate: #3b4a55;
    --ink: #3d4650;
    --accent: #1b8bb6;
    --rule: #4a535b;
  }
  * { margin: 0; padding: 0; box-sizing: border-box; }
  html, body {
    width: 1200px; height: 720px; overflow: hidden;
    background: var(--backdrop);
    font-family: "Lato", sans-serif;
  }
  .canvas { position: relative; width: 1200px; height: 720px; }
  .card {
    position: absolute; top: 242px;
    width: 420px; height: 239px;
    background: var(--card);
    box-shadow: 0 6px 18px rgba(0,0,0,0.18);
  }
  .card--front { left: 147px; }
  .card--back { left: 633px; }

  .brand { position: absolute; width: 98px; text-align: center; }
  .card--front .brand { left: 63px; top: 70px; }
  .card--back .brand { left: 161px; top: 70px; }
  .brand__square { display: block; width: 98px; height: 79px; background: var(--slate); }
  .brand__name {
    display: block; margin-top: 8px;
    font-size: 12.5px; font-weight: 400; letter-spacing: 0.3px;
    color: var(--slate); white-space: nowrap;
  }

  .divider {
    position: absolute; left: 185px; top: 58px;
    width: 1.5px; height: 128px; background: var(--rule);
  }

  .contact { position: absolute; left: 202px; top: 70px; color: var(--ink); }
  .contact__name { font-size: 13.5px; font-weight: 700; color: var(--accent); line-height: 16px; }
  .contact__role { font-size: 10.5px; line-height: 13px; }
  .contact__address { margin-top: 12px; font-size: 10.5px; line-height: 12.5px; }
  .contact__lines { margin-top: 15px; list-style: none; font-size: 10.5px; line-height: 12.5px; }
  .contact__lines li { display: flex; align-items: center; gap: 7px; }
  .contact__lines svg { width: 11px; height: 9px; fill: var(--accent); flex: none; }
</style>
</head>
<body>
<main class="canvas">
  <section class="card card--front">
    <div class="brand">
      <span class="brand__square"></span>
      <span class="brand__name">KLT ROOFING</span>
    </div>
    <div class="divider"></div>
    <div class="contact">
      <p class="contact__name">Corran Hale</p>
      <p class="contact__role">General Manager</p>
      <p class="contact__address">218 Wexford Lane, Port<br>Ashby</p>
      <ul class="contact__lines">
        <li>
          <svg viewBox="0 0 12 10" aria-hidden="true"><path d="M1 3.5C1 1.5 3 1 6 1s5 .5 5 2.5v1H8.5V3H3.5v1.5H1z M3 5h6l1.5 4h-9z"/></svg>
          0400 555 921
        </li>
        <li>
          <svg viewBox="0 0 12 10" aria-hidden="true"><path d="M0 1h12v8H0z M1 2l5 3.6L11 2" stroke="#fbfbfb" stroke-width="0.9"/></svg>
          chale@kltsteelroofing.com.au
        </li>
      </ul>
    </div>
  </section>

  <section class="card card--back">
    <div class="brand">
      <span class="brand__square"></span>
      <span class="brand__name">KLT ROOFING</span>
    </div>
  </section>
</main>
</body>
</html>
```